The Polish & Sugar Loft Website Update

Hello. I am seeking to freshen up my website with a clean and easy feel that incorporates our modern chic style. Our services cater to mostly young professionals and modern moms.

We focus on natural nail care and gentle professional waxing. We are known for our cleanliness. Our clients like our current website, however I'm hoping to make it look even more professional and user friendly. Some clients have even said our current website feels welcoming, unlike other websites that in they feel give a snobbish vibe. I like clean lines, simple, fresh, and sometimes bold. Totally NOT a fan of whimsical.

I threw added an accent color to the color pallet...however it should be used in moderation. I am also open to other accent colors. I'd like the site to emphasize the Brazilian wax as much as nails, if not more than nail. The photos downloaded are just to give you a few images of who we are, however are not necessary. Current website www.polishsugarloft-demo.com

Target Market(s)

Females 30-55

Industry/Entity Type

Beauty Salon

Coding

Coded - Design and coding required

Number of Pages Required

5+ page

Font styles to use
Sans Serif

Colors
ffffff
1b1b1b
acd136
eeeeee
878787
c4c4c4
efefef
7f7f7f

Requirements
Must have
• Clean look
Nice to have
• Our logo
Should not have
• Whimsical

```html
<!DOCTYPE html>
<html lang="en">
<head>
<meta charset="utf-8">
<title>The Polish &amp; Sugar Loft</title>
<link href="https://fonts.googleapis.com/css2?family=Questrial&display=swap" rel="stylesheet">
<style>
:root{
  --white:#ffffff;
  --ink:#1b1b1b;
  --lime:#acd136;
  --panel:#eeeeee;
  --grey:#878787;
  --line:#c4c4c4;
  --soft:#efefef;
  --mid:#7f7f7f;
  --text:#555555;
  --dark-band:#262626;
  --footer:#202020;
}
*{box-sizing:border-box;margin:0;padding:0}
html,body{width:694px;height:1200px;overflow:hidden;background:var(--white)}
body{font-family:"Questrial",sans-serif;color:var(--text);position:relative}
.abs{position:absolute}

/* header */
.brand{left:77px;top:20px;font-size:20px;color:var(--grey);display:flex;align-items:center;gap:7px;letter-spacing:.2px}
.brand-mark{width:12px;height:12px;background:var(--lime)}
.social{display:flex;gap:6px}
.social span{width:15px;height:15px;border-radius:50%;background:var(--line);display:block}
.header-social{left:373px;top:22px}
.header-btn{top:16px;height:26px;border:1px solid var(--line);border-radius:2px;font-size:7px;color:var(--grey);text-align:center;line-height:8px;padding-top:5px;padding-right:16px}
.header-btn svg{position:absolute;right:5px;top:6px}
.btn-schedule{left:433px;width:90px}
.btn-gift{left:528px;width:89px}

/* nav */
.nav{left:77px;top:60px;width:540px;height:25px;background:var(--lime);display:flex;align-items:center;font-size:8px;color:var(--ink);z-index:2}
.nav a{color:inherit;text-decoration:none;padding:0 12px;line-height:25px}
.nav a.active{background:#444;color:var(--white);padding:0 14px}

/* hero */
.hero{left:0;top:73px;width:694px;height:281px;background:linear-gradient(160deg,#f3f1ee 0%,#e7e3de 45%,#d9d3cc 100%)}
.hero-hands{left:150px;top:0;width:400px;height:270px;background:radial-gradient(ellipse at 50% 40%,#e8b9a6 0%,#e4b4a0 35%,rgba(228,180,160,0) 70%)}
.hero-caption{right:77px;top:282px;text-align:right;font-size:15px;line-height:18px;color:#555}
.hero-caption b{font-weight:400;color:var(--lime)}
.hero-arrow{top:206px}

/* mission */
.h2{font-size:19px;color:var(--ink);font-weight:400}
.mission-title{left:77px;top:381px}
.menu-title{right:77px;top:381px}
.mission-copy{left:77px;top:410px;width:175px;font-size:6px;line-height:12px;color:#666}
.mission-copy p+p{margin-top:6px}
.salon-photo{left:262px;top:412px;width:176px;height:153px;background:linear-gradient(135deg,#cfc9c0 0%,#8d8781 50%,#4a4743 100%)}
.menu-box{left:447px;width:170px;background:var(--panel);padding:8px 9px}
.menu-nails{top:412px;height:75px}
.menu-wax{top:491px;height:75px}
.menu-box h3{font-size:10px;font-weight:400;color:var(--lime);margin-bottom:6px}
.menu-box ul{list-style:none;font-size:6.5px;color:#444;line-height:14px}
.wax-grid{display:grid;grid-template-columns:1fr 1fr;font-size:6.5px;line-height:16px;color:#444}
.wax-grid .more{color:var(--lime)}

.divider{left:77px;top:591px;width:540px;height:1px;background:#e2e2e2}
.appt-title{left:0;width:694px;top:612px;text-align:center;font-size:14px;color:var(--ink)}
.appt-btn{left:293px;top:638px;width:108px;height:25px;border:1px solid var(--line);text-align:center;line-height:23px;font-size:7.5px;color:#333}
.hours{left:0;width:694px;top:675px;text-align:center;font-size:7px;color:#333;word-spacing:1px}

/* facials band */
.facials{left:0;top:710px;width:694px;height:148px;background:linear-gradient(90deg,#1d1d1d 0%,#2e2e2e 55%,#202020 100%)}
.facial-photo{left:130px;top:740px;width:88px;height:88px;border-radius:50%;background:radial-gradient(circle at 45% 40%,#f0f0ee 0%,#d8cfc8 55%,#b9ada3 100%);border:2px solid #ddd}
.facial-title{left:235px;top:742px;font-size:14px;color:var(--lime)}
.facial-copy{left:235px;top:765px;width:350px;font-size:6px;line-height:12px;color:#ccc}
.book-btn{left:235px;top:796px;width:64px;height:25px;border:1px solid #888;color:#ddd;font-size:9px;text-align:center;line-height:23px}

/* reviews */
.reviews-title{left:0;width:694px;top:882px;text-align:center;font-size:13px;color:var(--lime)}
.quote{left:110px;width:474px;top:906px;text-align:center;font-size:10px;line-height:16px;color:#666}
.qmark{font-size:22px;color:var(--line);line-height:10px;vertical-align:-7px}
.reviewer{left:0;width:694px;top:948px;text-align:center;font-size:7px;color:#444}
.stars{left:318px;top:965px;display:flex;gap:1px}
.dots{left:323px;top:988px;display:flex;gap:10px}
.dots span{width:3px;height:3px;border-radius:50%;background:#999}
.dots span:first-child{background:var(--lime)}

/* footer */
.footer{left:0;top:1019px;width:694px;height:181px;background:var(--footer)}
.foot-title{top:1034px;font-size:10px;color:var(--lime)}
.offer{left:77px;top:1050px;width:258px;height:69px;background:linear-gradient(90deg,#3fb6e0 0%,#7fd2ee 55%,#d9c2a8 100%);overflow:hidden}
.offer-ribbon{left:-16px;top:12px;width:70px;height:10px;background:#d23a3a;transform:rotate(-45deg);color:var(--white);font-size:5px;text-align:center;line-height:10px}
.offer-text{left:24px;top:20px;font-size:9px;line-height:12px;color:var(--ink);font-weight:400}
.map{left:358px;top:1050px;width:107px;height:69px;background:linear-gradient(135deg,#eceae4,#dedbd3)}
.contact-card{left:465px;top:1050px;width:152px;height:69px;background:var(--white);padding:10px 12px;font-size:6px;color:#444;line-height:19px}
.contact-card div{display:flex;align-items:center;gap:6px}
.foot-line{left:77px;top:1145px;width:540px;height:1px;background:#3a3a3a}
.foot-links{left:77px;top:1160px;font-size:6px;color:#888;word-spacing:1px}
.copyright{left:77px;top:1176px;font-size:6px;color:#888}
.foot-social{left:564px;top:1164px}
.foot-social span{width:14px;height:14px;background:#666}
.foot-social span:first-child{background:#3b5a9a}
</style>
</head>
<body>

<header>
  <div class="abs brand"><span class="brand-mark"></span>The Polish &amp; Sugar Loft</div>
  <div class="abs social header-social" aria-label="Social links"><span></span><span></span><span></span></div>
  <div class="abs header-btn btn-schedule">Click here to<br>Schedule online!
    <svg width="11" height="11" viewBox="0 0 12 12" fill="none" stroke="#777" stroke-width="1"><rect x="1" y="2" width="8" height="9"/><path d="M5 8l6-6"/></svg>
  </div>
  <div class="abs header-btn btn-gift">Purchase<br>Gift Cards Online
    <svg width="11" height="11" viewBox="0 0 12 12" fill="none" stroke="#777" stroke-width="1"><rect x="1.5" y="4" width="9" height="7"/><path d="M1 4h10M6 4v7M6 4C4 1 2 2 4 4M6 4c2-3 4-2 2 0"/></svg>
  </div>
</header>

<nav class="abs nav">
  <a class="active">Home</a><a>Schedule An Appointment</a><a>Products and Services</a><a>Careers</a><a>Specials</a><a>About Us</a><a>FAQ</a><a>Contact Us</a>
</nav>

<section class="abs hero" role="img" aria-label="Close-up photo of hands with a natural French manicure on a white towel">
  <div class="abs hero-hands"></div>
</section>
<svg class="abs hero-arrow" style="left:18px" width="10" height="16" viewBox="0 0 10 16"><path d="M8 1L2 8l6 7" fill="none" stroke="#999" stroke-width="1.5"/></svg>
<svg class="abs hero-arrow" style="left:666px" width="10" height="16" viewBox="0 0 10 16"><path d="M2 1l6 7-6 7" fill="none" stroke="#999" stroke-width="1.5"/></svg>
<div class="abs hero-caption">The <b>#1</b> nail and wax salon<br>in the Fairview</div>

<section>
  <h2 class="abs h2 mission-title">Our Mission</h2>
  <div class="abs mission-copy">
    <p>To be the #1 nail and wax salon in the Fairview, CT area, offering the most meticulous manicures, pedicures, and waxing service. We use superior products, advanced techniques, and exceptional sanitation procedures to provide our clients with safe, quality services. Our knowledgeable and friendly staff is always happy to assist with any of your Nail &amp; Wax concerns.</p>
    <p>We are excited to welcome another Licensed Nail Technician to our team, Dana Whitfield. Dana has over 25 years experience and is also a certified Medical Nail Technician. You will love her spunk and genuine friendliness. If you're seeking a perfect mani, Dana is your girl.</p>
  </div>
  <div class="abs salon-photo" role="img" aria-label="Photo of the salon interior with pedicure chairs and polish wall"></div>

  <h2 class="abs h2 menu-title">Service Menu</h2>
  <div class="abs menu-box menu-nails">
    <h3>~Nails~</h3>
    <ul><li>Signature Manicure- $24</li><li>Gel Polish Manicure - $34</li><li>Signature Pedicure - $40</li></ul>
  </div>
  <div class="abs menu-box menu-wax">
    <h3>~Wax~</h3>
    <div class="wax-grid">
      <span>Brow Design - $13</span><span>Brazilian $55</span>
      <span>Chin - $10</span><span>Men Welcomed</span>
      <span>Lip - $10</span><span class="more">View More Services &nbsp;»</span>
    </div>
  </div>
</section>

<div class="abs divider"></div>
<h2 class="abs appt-title">Services By Appointment Only</h2>
<div class="abs appt-btn">Appointments Available</div>
<div class="abs hours">DAILY &nbsp; | &nbsp; 9am-8pm most days &nbsp; | &nbsp; Salon is only staffed for scheduled appointments.</div>

<section class="abs facials" role="img" aria-label="Dim photo of a treatment room"></section>
<div class="abs facial-photo" role="img" aria-label="Photo of a client receiving a facial mask"></div>
<h2 class="abs facial-title">Facials are now available at The Polish &amp; Sugar Loft</h2>
<p class="abs facial-copy">Our Signature Facial is meticulously customized to your skin's needs, be it quenching your skin's thirst, clearing unflattering breakouts, or repairing sun damage and fine lines.</p>
<div class="abs book-btn">Book Now</div>

<h2 class="abs reviews-title">Reviews</h2>
<p class="abs quote"><span class="qmark">“</span> What a great place. Excellent waxing job for a reasonable price. It was my first time there but I will definitely go back! <span class="qmark">”</span></p>
<div class="abs reviewer">Marisa L. Riverton, NY</div>
<div class="abs stars" aria-label="5 stars">
  <svg width="58" height="11" viewBox="0 0 58 11">
    <g fill="#d0161e"><rect x="0" width="11" height="11"/><rect x="11.7" width="11" height="11"/><rect x="23.4" width="11" height="11"/><rect x="35.1" width="11" height="11"/><rect x="46.8" width="11" height="11"/></g>
    <g fill="#fff"><path id="s" d="M5.5 1.5l1.2 2.6 2.8.3-2.1 1.9.6 2.8-2.5-1.4-2.5 1.4.6-2.8-2.1-1.9 2.8-.3z"/>
    <use href="#s" x="11.7"/><use href="#s" x="23.4"/><use href="#s" x="35.1"/><use href="#s" x="46.8"/></g>
  </svg>
</div>
<div class="abs dots"><span></span><span></span><span></span><span></span></div>

<footer class="abs footer"></footer>
<h3 class="abs foot-title" style="left:77px;font-weight:400">Special Offer</h3>
<div class="abs offer" role="img" aria-label="Photo of a woman in sunglasses relaxing by the pool">
  <div class="abs offer-ribbon">Special Offer</div>
  <div class="abs offer-text">Mauris vulputate<br>lobortis</div>
</div>
<h3 class="abs foot-title" style="left:358px;font-weight:400">Contact Info</h3>
<div class="abs map" role="img" aria-label="Street map showing the salon location"></div>
<address class="abs contact-card" style="font-style:normal">
  <div><svg width="6" height="8" viewBox="0 0 6 8"><path d="M3 0a3 3 0 0 0-3 3c0 2 3 5 3 5s3-3 3-5a3 3 0 0 0-3-3z" fill="#555"/><circle cx="3" cy="3" r="1" fill="#fff"/></svg>42 Maple Lane, Fairview, CT 06000</div>
  <div><svg width="6" height="7" viewBox="0 0 6 7"><path d="M1 0h1.5l.5 2-1 .7a4 4 0 0 0 1.8 1.8l.7-1 2 .5V5.5A1 1 0 0 1 5 6.5 5 5 0 0 1 0 1.5 1 1 0 0 1 1 0z" fill="#555"/></svg>ph: (555) 014-2298</div>
  <div><svg width="7" height="5" viewBox="0 0 7 5"><rect width="7" height="5" fill="#555"/><path d="M0 0l3.5 2.8L7 0" fill="none" stroke="#fff" stroke-width=".6"/></svg>hello@polishsugarloft-demo.com</div>
</address>
<div class="abs foot-line"></div>
<div class="abs foot-links">Home &nbsp;| &nbsp;Schedule An Appointment &nbsp;| &nbsp;Products and Services &nbsp;| &nbsp;Careers &nbsp;| &nbsp;Specials &nbsp;| &nbsp;About Us &nbsp;| &nbsp;FAQ &nbsp;| &nbsp;Contact Us</div>
<div class="abs copyright">Copyright © 2016 &nbsp;The Polish &amp; Sugar Loft. &nbsp;All rights reserved.</div>
<div class="abs social foot-social" aria-label="Social links"><span></span><span></span><span></span></div>

</body>
</html>
```